Rebranding our business - Business Cards

We are currently rebranding our business and have just completed our new logo and now are wanting to have new business cards designed.

I will upload our old business card design as we would like to keep the same information on the card, Including the icon dot points on the back. I will also upload other designs I would like placed on the cards.. Such as a character,

I would like our power statement to be:
TKJ Removals -The Steady Haulers.

Instead of: Let TKJ Removals Carry Every Box Through Your Big Day,

I am happy for the designer to run with their own ideas.

```html
<!DOCTYPE html>
<html lang="en">
<head>
<meta charset="utf-8">
<title>TKJ Removals – Business Cards</title>
<link rel="stylesheet" href="https://fonts.googleapis.com/css2?family=Open+Sans:wght@400;600;700&display=swap">
<style>
  :root {
    --navy: #2b3381;
    --navy-deep: #1d2262;
    --ink: #3b4688;
    --blue: #3f8fd0;
    --orange: #f26a2b;
    --white: #ffffff;
    --map-grey: #e4e6ee;
    --stage: #ececef;
  }
  * { box-sizing: border-box; margin: 0; padding: 0; }
  html, body { width: 1200px; height: 913px; overflow: hidden; }
  body {
    background: var(--stage);
    font-family: "Open Sans", Arial, sans-serif;
    position: relative;
  }
  .card {
    position: absolute;
    top: 300px;
    width: 540px;
    height: 310px;
    border-radius: 16px;
    overflow: hidden;
    box-shadow: 0 8px 24px rgba(0,0,0,.18);
  }
  .card--front { left: 30px; background: var(--white); }
  .card--back {
    left: 630px;
    background: linear-gradient(160deg, var(--navy) 0%, var(--navy-deep) 100%);
    color: var(--white);
  }

  /* front */
  .front-map {
    position: absolute; right: 0; top: 60px; width: 250px; height: 250px;
    background: radial-gradient(ellipse at 60% 55%, var(--map-grey) 0%, rgba(228,230,238,.35) 70%, transparent 100%);
  }
  .corner-tab {
    position: absolute; right: -10px; top: -10px; width: 36px; height: 36px;
    border: 3px solid var(--blue); border-radius: 10px; background: var(--orange);
  }
  .owner { position: absolute; right: 40px; top: 30px; text-align: right; }
  .owner__name { font-size: 22px; font-weight: 700; color: var(--ink); line-height: 1.1; }
  .owner__role { font-size: 13px; color: var(--blue); line-height: 1.3; }
  .rule { position: absolute; height: 1px; background: var(--orange); }
  .rule--owner { left: 320px; right: 0; top: 82px; }
  .brand {
    position: absolute; display: flex; align-items: center; gap: 10px;
    font-size: 34px; font-weight: 600; line-height: 1;
  }
  .brand__dot { width: 16px; height: 16px; border-radius: 50%; }
  .card--front .brand { left: 30px; top: 96px; color: var(--blue); }
  .card--front .brand__dot { background: var(--navy); }
  .power {
    position: absolute; left: 30px; top: 146px;
    font-size: 13px; font-weight: 700; color: var(--blue); letter-spacing: .3px;
  }
  .power__name { color: var(--ink); }
  .address { position: absolute; right: 30px; top: 176px; font-size: 13px; color: var(--ink); }
  .contact-head {
    position: absolute; left: 30px; top: 190px;
    font-size: 13px; font-weight: 700; color: var(--ink);
  }
  .rule--contact { left: 0; width: 140px; top: 210px; }
  .contacts { position: absolute; left: 30px; top: 218px; list-style: none; }
  .contacts li { display: flex; align-items: center; gap: 8px; font-size: 13px; color: var(--ink); line-height: 17px; }
  .contacts svg { width: 11px; height: 11px; fill: var(--navy); flex: none; }

  /* back */
  .insurance { position: absolute; right: 30px; top: 24px; font-size: 13px; font-weight: 600; letter-spacing: .3px; }
  .back-contacts { position: absolute; right: 30px; top: 52px; list-style: none; text-align: right; }
  .back-contacts li { display: flex; justify-content: flex-end; align-items: center; gap: 8px; font-size: 13px; line-height: 18px; }
  .back-contacts svg { width: 11px; height: 11px; fill: var(--orange); flex: none; }
  .rule--back { left: 210px; right: 0; top: 136px; }
  .card--back .brand { left: 30px; top: 150px; color: var(--white); }
  .card--back .brand__dot { background: var(--orange); }
  .provides { position: absolute; left: 30px; top: 198px; font-size: 13px; }
  .services { list-style: none; margin-top: 4px; }
  .services li { display: flex; align-items: center; gap: 8px; font-size: 13px; line-height: 16px; }
  .services svg { width: 10px; height: 10px; fill: var(--orange); flex: none; }
  .mascot {
    position: absolute; right: 30px; bottom: 40px; width: 140px; height: 110px;
    border-radius: 10px;
    background: linear-gradient(180deg, rgba(242,106,43,.55), rgba(120,130,180,.45));
  }
</style>
</head>
<body>

<section class="card card--front">
  <div class="front-map" role="img" aria-label="Faint grey world map decoration"></div>
  <div class="corner-tab"></div>
  <div class="owner">
    <p class="owner__name">Marcus Delaney</p>
    <p class="owner__role">Owner Operator</p>
  </div>
  <div class="rule rule--owner"></div>
  <div class="brand"><span class="brand__dot"></span>TKJ Removals</div>
  <p class="power"><span class="power__name">TKJ REMOVALS</span> -THE STEADY HAULERS</p>
  <p class="address">Harbour Bay, QLD 4230</p>
  <p class="contact-head">TKJ REMOVALS</p>
  <div class="rule rule--contact"></div>
  <ul class="contacts">
    <li><svg viewBox="0 0 10 10"><rect x="2" y="0" width="6" height="10" rx="1"/></svg>0412 738 604</li>
    <li><svg viewBox="0 0 10 10"><path d="M1 4q4-4 8 0v2H7V5H3v1H1z M2 6h6l1 4H1z"/></svg>07 5520 4831</li>
    <li><svg viewBox="0 0 10 10"><path d="M0 2h10v6H0z"/></svg>tkjremovals@mailbox.com</li>
    <li><svg viewBox="0 0 10 10"><circle cx="5" cy="5" r="5"/></svg>www.tkjremovals.com.au</li>
    <li><svg viewBox="0 0 10 10"><rect width="10" height="10" rx="2"/></svg>www.chatterpage.com/tkjremovals</li>
  </ul>
</section>

<section class="card card--back">
  <p class="insurance">FREE TRANSIT INSURANCE</p>
  <ul class="back-contacts">
    <li>0412 738 604<svg viewBox="0 0 10 10"><rect x="2" y="0" width="6" height="10" rx="1"/></svg></li>
    <li>07 5520 4831<svg viewBox="0 0 10 10"><path d="M1 4q4-4 8 0v2H7V5H3v1H1z M2 6h6l1 4H1z"/></svg></li>
    <li>tkjremovals@mailbox.com<svg viewBox="0 0 10 10"><path d="M0 2h10v6H0z"/></svg></li>
    <li>www.tkjremovals.com.au<svg viewBox="0 0 10 10"><circle cx="5" cy="5" r="5"/></svg></li>
  </ul>
  <div class="rule rule--back"></div>
  <div class="brand"><span class="brand__dot"></span>TKJ Removals</div>
  <div class="provides">
    <p>TKJ Removals Provides:</p>
    <ul class="services">
      <li><svg viewBox="0 0 10 10"><path d="M0 4h7v5H0z M7 6h3v3H7z"/></svg>Local, Country &amp; Interstate Removals</li>
      <li><svg viewBox="0 0 10 10"><path d="M5 0l5 5H8v5H2V5H0z"/></svg>Home &amp; Hi Rise Removals</li>
      <li><svg viewBox="0 0 10 10"><path d="M0 10V3l3 2V3l3 2V0h4v10z"/></svg>Office &amp; Factory Relocation's</li>
      <li><svg viewBox="0 0 10 10"><path d="M0 2h10v8H0z"/></svg>Pre - Packing &amp; Unpacking Service's</li>
      <li><svg viewBox="0 0 10 10"><path d="M0 3l5-3 5 3v7H0z"/></svg>Storage Solution</li>
    </ul>
  </div>
  <div class="mascot" role="img" aria-label="Cartoon removalist character with a hand trolley and boxes"></div>
</section>

</body>
</html>
```